Business Card Makeover. Recreate a sleek modern design for our business card.

DO NOT COPY OUR CURRENT DESIGN. MUST BE ONE SIDED BUSINESS CARD.
Create a new business card design, using our new logo. Attached is a sample of our current design and new logo. Please note the address and email will change. The new address is 417 Corvell West Palm Beach 33472 and our website will be www.talvendrake.example.

We are an architectural and interior design firm. We prefer a clean modern look. Something that is refined and emulates excellence.

Industry/Entity Type

Architecture

Contact Information for Business Card

clean modern look, please do not copy our attached design.

Font styles to use
Other font styles liked:
• see attached business card font

Colors

Designer to choose colors to be used in the design.

Requirements
Must have
• Must have a modern appeal and resemble our current branding.
Nice to have
• modern font, our logo, legible name and titles progressive design
Should not have
• Do not add colors not reflected in our branding. Should not look like our current card.

```html
<!DOCTYPE html>
<html lang="en">
<head>
<meta charset="utf-8">
<title>Talvendrake + Partners – Business Cards</title>
<link rel="stylesheet" href="https://fonts.googleapis.com/css2?family=Source+Sans+3:wght@400;700&display=swap">
<style>
  :root {
    --page-bg: #e6e7e9;
    --card-bg: #ffffff;
    --ink: #231f20;
    --brand-blue: #1f5fae;
    --deep-blue: #2453a6;
    --sky-blue: #4cc6f0;
  }
  * { margin: 0; padding: 0; box-sizing: border-box; }
  html, body {
    width: 1200px; height: 1200px; overflow: hidden;
    background: var(--page-bg);
    font-family: "Source Sans 3", "Myriad Pro", sans-serif;
    color: var(--ink);
  }
  .business-card {
    position: absolute; left: 248px;
    width: 733px; height: 469px;
    background: var(--card-bg);
    overflow: hidden;
  }
  .business-card--first { top: 101px; }
  .business-card--second { top: 630px; }
  .accent-area { position: absolute; inset: 0; }
  .brand {
    position: absolute; left: 70px; top: 53px;
    display: flex; align-items: center; gap: 12px;
  }
  .brand-dot {
    width: 62px; height: 62px; border-radius: 50%;
    background: var(--brand-blue);
  }
  .brand-name {
    font-size: 22px; font-weight: 400; letter-spacing: 0.5px;
    color: var(--brand-blue); line-height: 1;
  }
  .person { position: absolute; left: 70px; top: 144px; }
  .person-name { font-size: 22px; font-weight: 700; line-height: 28px; }
  .person-title { font-size: 22px; font-weight: 400; line-height: 28px; }
  .contact-lines, .firm-details {
    position: absolute; right: 69px; text-align: right;
    font-size: 19px; line-height: 24.5px;
  }
  .contact-lines { top: 56px; }
  .firm-details { top: 283px; }
  .firm-discipline { margin-bottom: 11px; }
  .registered { font-size: 10px; }
</style>
</head>
<body>

<svg width="0" height="0" style="position:absolute" aria-hidden="true">
  <defs>
    <linearGradient id="accent-fill" x1="0" y1="0" x2="1" y2="0">
      <stop offset="0" stop-color="#2453a6"/>
      <stop offset="0.6" stop-color="#4cc6f0"/>
      <stop offset="1" stop-color="#ffffff"/>
    </linearGradient>
  </defs>
</svg>

<section class="business-card business-card--first">
  <svg class="accent-area" viewBox="0 0 733 469" role="img" aria-label="Decorative soft blue gradient area rising to the right">
    <polygon points="38,434 691,434 691,93" fill="url(#accent-fill)"/>
  </svg>
  <div class="brand">
    <span class="brand-dot"></span>
    <span class="brand-name">TALVENDRAKE + PARTNERS</span>
  </div>
  <div class="contact-lines">
    <p>office: 561.555.0142</p>
    <p>fax: 561.555.0187</p>
    <p>cell: 561.555.0123</p>
  </div>
  <div class="person">
    <p class="person-name">Marcus Ellery</p>
    <p class="person-title">Partner / Director of Design</p>
  </div>
  <div class="firm-details">
    <p class="firm-discipline">Architecture + Interior Design</p>
    <p>417 Corvell</p>
    <p>West Palm Beach 33472</p>
    <p>www.talvendrake.example</p>
    <p>LIC.# AA48170526</p>
  </div>
</section>

<section class="business-card business-card--second">
  <svg class="accent-area" viewBox="0 0 733 469" role="img" aria-label="Decorative soft blue gradient area rising to the right">
    <polygon points="38,434 691,434 691,93" fill="url(#accent-fill)"/>
  </svg>
  <div class="brand">
    <span class="brand-dot"></span>
    <span class="brand-name">TALVENDRAKE + PARTNERS</span>
  </div>
  <div class="contact-lines">
    <p>office: 561.555.0142</p>
    <p>fax: 561.555.0187</p>
  </div>
  <div class="person">
    <p class="person-name">Renata Vessler, AIA, LEED<sup class="registered">®</sup> AP</p>
    <p class="person-title">Partner / Project Architect</p>
  </div>
  <div class="firm-details">
    <p class="firm-discipline">Architecture + Interior Design</p>
    <p>417 Corvell</p>
    <p>West Palm Beach 33472</p>
    <p>www.talvendrake.example</p>
    <p>LIC.# AA48170526</p>
  </div>
</section>

</body>
</html>
```